Brightstep Foot Care Advertisement Sandwich board

We need a Sandwich board design for our fungal nail clinic - please find attached the sandwich board dimensions.

The sandwich board itself will be displayed outside of a large health clinic and we need it to attract the attention of people walking by. We need a brochure holder included in the design which will hold our brochures which provides as clients with more information (please see attached also).

We are open to the designers creativity but we would like a similar theme portrayed on our board that is similar to our website (www.brightstepfootcare.co.nz) and brochure that incorporates our logo which I have attached). The final design should communicate professionalism and be a minimalist look but modern to capture the attention of pedestrians.

Finally, we would like the website and phone number (07) 312 5840.

We look forward to seeing your work.

```html
<!DOCTYPE html>
<html lang="en">
<head>
<meta charset="utf-8">
<title>Brightstep Foot Care – Sandwich Board</title>
<link rel="stylesheet" href="https://fonts.googleapis.com/css2?family=Montserrat:wght@400;500;600;700;800&display=swap">
<style>
  :root {
    --brand-blue: #2f5fb3;
    --brand-navy: #1f2f5c;
    --band-grey: #c9ccd3;
    --paper: #ffffff;
    --paper-tint: #f3f5f9;
    --skin-light: #f1ddd2;
    --skin-mid: #e2bfae;
    --text-white: #ffffff;
  }
  * { margin: 0; padding: 0; box-sizing: border-box; }
  html, body { width: 900px; height: 1200px; overflow: hidden; background: var(--paper); }
  body { font-family: "Montserrat", Arial, sans-serif; }

  .board {
    position: relative;
    width: 900px;
    height: 1200px;
    overflow: hidden;
    background: linear-gradient(160deg, var(--paper) 40%, var(--paper-tint) 100%);
  }

  .hero-photo {
    position: absolute;
    left: 0; top: 0;
    width: 600px; height: 1000px;
    background: radial-gradient(ellipse at 40% 45%, var(--skin-mid) 0%, var(--skin-light) 45%, var(--paper) 85%);
  }

  .swoosh { position: absolute; left: 0; top: 0; width: 900px; height: 1200px; }

  .brand {
    position: absolute;
    left: 600px; top: 150px;
    display: flex; align-items: center; gap: 14px;
  }
  .brand-dot {
    width: 46px; height: 46px; border-radius: 50%;
    background: var(--brand-blue);
    flex: none;
  }
  .brand-name {
    font-weight: 600; font-size: 21px; line-height: 1.15;
    color: var(--brand-navy); letter-spacing: 0.5px; text-transform: uppercase;
  }

  .headline {
    position: absolute;
    left: 570px; top: 400px;
    line-height: 0.95;
  }
  .headline-lead { display: block; font-weight: 600; font-size: 36px; color: var(--brand-navy); letter-spacing: 1px; margin-bottom: 8px; }
  .headline-fungal { display: block; font-weight: 800; font-size: 78px; color: var(--brand-blue); }
  .headline-nail { display: block; font-weight: 800; font-size: 118px; color: var(--brand-blue); }
  .headline-experts { display: block; font-weight: 700; font-size: 62px; color: var(--brand-navy); margin-top: 4px; }

  .contact-phone {
    position: absolute;
    left: 250px; top: 1020px;
    display: flex; align-items: center; gap: 18px;
    color: var(--text-white); font-weight: 700; font-size: 48px;
  }
  .contact-phone svg { width: 44px; height: 44px; }

  .contact-web {
    position: absolute;
    left: 250px; top: 1105px;
    width: 560px; height: 52px; border-radius: 26px;
    background: var(--paper);
    display: flex; align-items: center; justify-content: center;
    color: var(--brand-navy); font-weight: 600; font-size: 22px;
  }
</style>
</head>
<body>
  <main class="board">
    <div class="hero-photo" role="img" aria-label="Photograph of a woman's smooth bare legs and feet with healthy toenails"></div>

    <svg class="swoosh" viewBox="0 0 900 1200" aria-hidden="true">
      <path d="M900 170 C900 690 690 935 0 945 L0 1200 L900 1200 Z" fill="var(--band-grey)"/>
      <path d="M900 195 C900 705 700 955 0 965 L0 1200 L900 1200 Z" fill="var(--paper)"/>
      <path d="M900 220 C900 725 710 975 0 985 L0 1200 L900 1200 Z" fill="var(--brand-blue)"/>
    </svg>

    <div class="brand">
      <span class="brand-dot"></span>
      <span class="brand-name">Brightstep<br>Foot Care</span>
    </div>

    <h1 class="headline">
      <span class="headline-lead">YOUR</span>
      <span class="headline-fungal">Fungal</span>
      <span class="headline-nail">Nail</span>
      <span class="headline-experts">Experts</span>
    </h1>

    <div class="contact-phone">
      <svg viewBox="0 0 24 24" aria-hidden="true"><path fill="#ffffff" d="M6.6 10.8a15.1 15.1 0 0 0 6.6 6.6l2.2-2.2c.3-.3.7-.4 1-.2 1.1.4 2.3.6 3.6.6.6 0 1 .4 1 1V20c0 .6-.4 1-1 1A17 17 0 0 1 3 4c0-.6.4-1 1-1h3.5c.6 0 1 .4 1 1 0 1.3.2 2.5.6 3.6.1.3 0 .7-.2 1z"/></svg>
      <span>(07) 312 5840</span>
    </div>

    <div class="contact-web">www.brightstepfootcare.co.nz</div>
  </main>
</body>
</html>
```